Packaging design for Virgin Coconut Oil. 100% pure cold pressed coconut oil

We need a new packaging and label design for our Virgin Coconut Oil product. It is currently marketed in the Philippines as a food supplement. We would like to try marketing it to other Asian countries such as Singapore, Malaysia and Hong Kong. The company has been producing this product since 2004 but now would like to venture into exporting our products overseas.

Would like to see designs with earth, natural "organic" colors. Fresh, Clean and pure look. Our trade mark is "Kestrel Meadow". Its a 100% pure cold pressed virgin coconut oil. All in all, we want to totally repackage our product and re-design the trademark to cater to export markets. Thanks!

Mid to High

Health Product

cadf82
9bcb3b
33b8a4
ffffff
3176b5
3276b5
0592cd
fbed22
fece3e

• Bottle shape design ideas.

```html
<!DOCTYPE html>
<html lang="en">
<head>
<meta charset="utf-8">
<title>Kestrel Meadow Virgin Coconut Oil Label</title>
<link rel="stylesheet" href="https://fonts.googleapis.com/css2?family=Libre+Caslon+Text:wght@400;700&family=Roboto+Condensed:wght@700&display=swap">
<style>
  :root {
    --bg: #ffffff;
    --gold-light: #f6e6a6;
    --gold-mid: #d4a94a;
    --gold-dark: #8a5f1c;
    --panel-deep: #06243a;
    --panel-mid: #0d4a6e;
    --panel-glow: #1c7aa3;
    --title: #ffffff;
    --accent-yellow: #fbed22;
    --band-text: #2f6b1c;
    --band-bg: #ffffff;
    --brand-ink: #6b2a12;
  }
  html, body {
    margin: 0;
    padding: 0;
    width: 1200px;
    height: 2656px;
    overflow: hidden;
    background: var(--bg);
  }
  .label {
    display: block;
    width: 1200px;
    height: 2656px;
  }
  .product-title {
    font-family: "Libre Caslon Text", Georgia, serif;
    font-weight: 400;
    fill: var(--title);
    text-anchor: middle;
  }
  .brand-name {
    font-family: "Libre Caslon Text", Georgia, serif;
    font-weight: 700;
    fill: var(--brand-ink);
    text-anchor: middle;
  }
  .grade {
    font-family: "Roboto Condensed", Arial, sans-serif;
    font-weight: 700;
    fill: var(--accent-yellow);
    text-anchor: middle;
  }
  .band-text {
    font-family: "Roboto Condensed", Arial, sans-serif;
    font-weight: 700;
    fill: var(--band-text);
    text-anchor: middle;
  }
</style>
</head>
<body>
<svg class="label" viewBox="0 0 408 903" width="1200" height="2656" xmlns="http://www.w3.org/2000/svg">
  <defs>
    <linearGradient id="goldFrame" x1="0" y1="0" x2="1" y2="1">
      <stop offset="0" stop-color="var(--gold-light)"/>
      <stop offset="0.35" stop-color="var(--gold-mid)"/>
      <stop offset="0.6" stop-color="var(--gold-dark)"/>
      <stop offset="0.85" stop-color="var(--gold-light)"/>
      <stop offset="1" stop-color="var(--gold-mid)"/>
    </linearGradient>
    <radialGradient id="panelGlow" cx="0.55" cy="0.42" r="0.7">
      <stop offset="0" stop-color="var(--panel-glow)"/>
      <stop offset="0.5" stop-color="var(--panel-mid)"/>
      <stop offset="1" stop-color="var(--panel-deep)"/>
    </radialGradient>
    <radialGradient id="brandBadge" cx="0.5" cy="0.4" r="0.6">
      <stop offset="0" stop-color="#fff3c2"/>
      <stop offset="1" stop-color="#c8953a"/>
    </radialGradient>
    <linearGradient id="coconutsFill" x1="0" y1="0" x2="1" y2="0">
      <stop offset="0" stop-color="#7fb43a"/>
      <stop offset="0.6" stop-color="#a9c96a"/>
      <stop offset="1" stop-color="#e9dcc3"/>
    </linearGradient>
    <linearGradient id="groveFill" x1="0" y1="0" x2="0" y2="1">
      <stop offset="0" stop-color="#cfe3a8"/>
      <stop offset="0.5" stop-color="#7fb43a"/>
      <stop offset="1" stop-color="#3f6e24"/>
    </linearGradient>
    <clipPath id="innerClip">
      <path d="M18,128 Q42,128 42,100 Q126,19 204,19 Q282,19 366,100 Q366,128 390,128 L390,850 Q362,850 362,884 L46,884 Q46,850 18,850 Z"/>
    </clipPath>
  </defs>

  <!-- outer gold frame -->
  <path class="frame-outer" fill="url(#goldFrame)"
        d="M4,122 Q30,122 30,94 Q120,4 204,4 Q288,4 378,94 Q378,122 404,122 L404,862 Q374,862 374,899 L34,899 Q34,862 4,862 Z"/>
  <path class="frame-rule" fill="#1a1206"
        d="M12,125 Q37,125 37,97 Q123,12 204,12 Q285,12 371,97 Q371,125 396,125 L396,856 Q368,856 368,892 L40,892 Q40,856 12,856 Z"/>

  <g clip-path="url(#innerClip)">
    <!-- blue panel -->
    <rect class="panel" x="0" y="0" width="408" height="903" fill="url(#panelGlow)"/>
    <path class="panel-sheen" d="M18,0 L260,0 Q150,250 18,520 Z" fill="#ffffff" opacity="0.06"/>

    <!-- stars -->
    <g class="stars" fill="#f2d27a">
      <polygon points="140,54 143.5,61 151,62 145.5,67 147,74.5 140,71 133,74.5 134.5,67 129,62 136.5,61"/>
      <polygon points="172,43 175.5,50 183,51 177.5,56 179,63.5 172,60 165,63.5 166.5,56 161,51 168.5,50"/>
      <polygon points="204,38 207.5,45 215,46 209.5,51 211,58.5 204,55 197,58.5 198.5,51 193,46 200.5,45"/>
      <polygon points="236,43 239.5,50 247,51 241.5,56 243,63.5 236,60 229,63.5 230.5,56 225,51 232.5,50"/>
      <polygon points="268,54 271.5,61 279,62 273.5,67 275,74.5 268,71 261,74.5 262.5,67 257,62 264.5,61"/>
    </g>

    <!-- brand name -->
    <circle class="brand-disc" cx="204" cy="190" r="64" fill="url(#brandBadge)"/>
    <text class="brand-name" x="204" y="185" font-size="21">Kestrel</text>
    <text class="brand-name" x="204" y="210" font-size="21">Meadow</text>

    <!-- product title -->
    <text class="product-title" x="204" y="348" font-size="58">Virgin</text>
    <text class="product-title" x="204" y="420" font-size="58">Coconut</text>
    <text class="product-title" x="204" y="492" font-size="58">Oil</text>

    <!-- coconut cluster -->
    <rect class="coconut-visual" role="img" aria-label="Fresh green coconuts, some cracked open showing white flesh"
          x="44" y="522" width="196" height="108" rx="50" fill="url(#coconutsFill)"/>

    <text class="grade" x="320" y="604" font-size="17">EXTRA VIRGIN</text>
    <text class="grade" x="320" y="622" font-size="12">NATURAL 100%</text>

    <!-- band -->
    <rect class="band-rule" x="0" y="642" width="408" height="4" fill="var(--gold-mid)"/>
    <rect class="band" x="0" y="646" width="408" height="24" fill="var(--band-bg)"/>
    <text class="band-text" x="204" y="664" font-size="15">100% Pure Cold Pressed Virgin Coconut Oil</text>

    <!-- coconut grove -->
    <rect class="grove-visual" role="img" aria-label="Bunch of green coconuts hanging on a palm tree with fronds"
          x="0" y="670" width="408" height="233" fill="url(#groveFill)"/>
  </g>
</svg>
</body>
</html>
```